Harbor Glow Living.com Landing Page

Create a well designed home/landing page using that communicates the feeling of Harbor Glow Living with this sections that scroll from top to bottom -
Top section - Displays "Harbor Glow Living" with space for embedded YouTube video.

The following sections follow the top section -
Assess your current Harbor Glow Living. Complete our free life balance assessment to identify key areas where you you will most benefit.
"Learn more" call to action button

Create a Harbor Glow Living Study Hub account. Get a 14 day free trial to a wealth of learning activities, motivational videos and professional presentations on our learning portal designed specifically to address the eight essential areas of Harbor Glow Living.
"Register now" call to action button

Get weekly reports on your progress and goal achievement. Celebrate your success each week as you review your progress on each life balance area.

Appropriate royalty free photos and graphics that fit the chosen theme you recommend.
Updates

I'm reviewing the designs. I realize that I need to clarify that Harbor Glow Living focuses on eight areas, not just physical fitness and meditation. Spirituality and Sense of Purpose; Fitness and Health; Relationships; Personal Finance; Recreation and Fun; Physical Environment; Personal Development and Learning; Work and Career

Number of Pages Required

1 page

Colors
33a6d7
00a990
9bcb3c
2f73b3

```html
<!DOCTYPE html>
<html lang="en">
<head>
<meta charset="utf-8">
<title>Harbor Glow Living</title>
<link href="https://fonts.googleapis.com/css2?family=Montserrat:wght@400;500;600;700&display=swap" rel="stylesheet">
<style>
:root{
  --ink:#141414;
  --text:#555a60;
  --blue:#2f73b3;
  --sky:#33a6d7;
  --teal:#00a990;
  --lime:#9bcb3c;
  --lime-soft:#d6e8bd;
  --mist:#f3f6f9;
  --line:#d9dde2;
  --white:#ffffff;
  --pink:#e5477d;
}
*{margin:0;padding:0;box-sizing:border-box}
html,body{width:1200px;height:2518px;overflow:hidden}
body{position:relative;background:var(--white);font-family:'Montserrat',sans-serif;color:var(--text)}
.abs{position:absolute}
.bg-layer{position:absolute;left:0;top:0}
.brand{display:flex;align-items:center;gap:10px}
.brand-dot{width:44px;height:44px;border-radius:50%;background:var(--teal)}
.brand-name{font-weight:700;font-size:19px;color:var(--ink);letter-spacing:.5px;line-height:1}
.btn{position:absolute;display:flex;align-items:center;justify-content:center;color:var(--white);font-weight:600;font-size:14px;letter-spacing:.2px;background:var(--blue);height:43px;text-decoration:none}
.btn-dark{background:#000}
.hero-title{position:absolute;left:100px;top:255px;border-left:3px solid var(--lime);padding-left:15px;font-weight:700;font-size:45px;line-height:46px;letter-spacing:2.5px;color:var(--ink);text-transform:uppercase}
.heading{position:absolute;border-left:3px solid var(--lime);padding-left:15px;font-weight:500;font-size:35px;line-height:43px;color:var(--ink)}
.copy{position:absolute;font-size:15.5px;line-height:25px;color:var(--text)}
.copy .big{font-size:28px;font-weight:700;color:var(--teal)}
.photo{position:absolute;border-radius:8px;box-shadow:0 6px 20px rgba(0,0,0,.18)}
.tilt{position:absolute;background:var(--lime-soft);border-radius:10px}
.play{position:absolute;left:838px;top:221px;width:63px;height:63px;border-radius:50%;background:var(--white);display:flex;align-items:center;justify-content:center}
.portal-screen{position:absolute;left:629px;top:1304px;width:469px;height:325px;border-radius:10px;box-shadow:0 6px 20px rgba(0,0,0,.12);background:linear-gradient(135deg,#ffffff,#eef0fb 60%,#e4f5ea)}
.footer-rule{position:absolute;left:99px;top:2464px;width:1002px;height:1px;background:var(--line)}
.legal{position:absolute;left:99px;top:2484px;font-size:12px;color:#666}
.social{position:absolute;top:2481px;width:18px;height:18px;border-radius:3px}
</style>
</head>
<body>

<svg class="bg-layer" width="1200" height="2518" viewBox="0 0 1200 2518" aria-hidden="true">
  <rect x="0" y="0" width="1200" height="654" fill="var(--mist)"/>
  <path d="M760,1290 C900,1200 1080,1170 1200,1168 L1200,1820 C1120,1750 1000,1720 880,1700 C760,1680 700,1560 740,1430 Z" fill="var(--mist)"/>
  <path d="M0,1742 C180,1730 330,1800 500,1840 C700,1885 900,1820 1200,1790 L1200,2282 L0,2282 Z" fill="var(--mist)"/>
  <path d="M640,0 C555,90 525,290 620,415 C710,530 860,525 1010,590 C1100,628 1160,648 1200,668 L1200,0 Z" fill="var(--lime-soft)"/>
</svg>
<svg class="bg-layer" width="1200" height="680" viewBox="0 0 1200 680" role="img" aria-label="Photo of a woman in jeans leaping from a rock above a green valley">
  <defs>
    <linearGradient id="valley" x1="0" y1="0" x2="1" y2="1">
      <stop offset="0" stop-color="#7fae4a"/>
      <stop offset=".55" stop-color="#5d9234"/>
      <stop offset="1" stop-color="#9cb85a"/>
    </linearGradient>
  </defs>
  <path d="M646,0 C560,90 532,285 625,405 C715,515 860,508 1010,570 C1100,606 1160,630 1200,646 L1200,0 Z" fill="url(#valley)"/>
</svg>

<header>
  <div class="abs brand" style="left:110px;top:14px">
    <span class="brand-dot"></span><span class="brand-name">HARBOR GLOW LIVING</span>
  </div>
  <a class="btn btn-dark" style="left:938px;top:16px;width:157px">REGISTER NOW</a>
</header>

<section class="hero">
  <div class="play"><svg width="16" height="16" viewBox="0 0 16 16"><path d="M3,1 L14,8 L3,15 Z" fill="var(--blue)"/></svg></div>
  <h1 class="hero-title">Harbor Glow<br>Living</h1>
  <p class="copy" style="left:108px;top:356px;width:390px">Giving you hope, inspiring you to take action and providing you with the tools and strategies to succeed.</p>
  <a class="btn" style="left:108px;top:451px;width:139px">LEARN MORE</a>
</section>

<section class="assess">
  <div class="tilt" style="left:90px;top:760px;width:460px;height:385px;transform:rotate(-15deg)"></div>
  <div class="photo" role="img" aria-label="Photo of a woman working on a laptop at a wooden desk" style="left:98px;top:780px;width:430px;height:345px;background:linear-gradient(120deg,#c9ced3,#8d959e 55%,#6b5140)"></div>
  <h2 class="heading" style="left:636px;top:834px;width:470px">Assess Your Current Harbor Glow Living.</h2>
  <p class="copy" style="left:634px;top:934px;width:450px">Complete our free life balance assessment to identify key areas where you you will most benefit.</p>
  <a class="btn" style="left:636px;top:1009px;width:139px">LEARN MORE</a>
</section>

<section class="portal">
  <h2 class="heading" style="left:100px;top:1306px;width:440px">Create a Harbor Glow Living Study Hub Account.</h2>
  <p class="copy" style="left:102px;top:1456px;width:390px">Get a <span class="big">14</span> day free trial to a wealth of learning activities, motivational videos and professional presentations on our learning portal designed specifically to address the eight essential areas of Harbor Glow Living.</p>
  <a class="btn" style="left:100px;top:1617px;width:147px">REGISTER NOW</a>
  <div class="tilt" style="left:615px;top:1285px;width:500px;height:370px;transform:rotate(-13deg)"></div>
  <div class="portal-screen" role="img" aria-label="Screenshot of the learning portal dashboard with profile, statistics, investments and balance panels"></div>
</section>

<section class="reports">
  <div class="tilt" style="left:95px;top:1845px;width:480px;height:410px;transform:rotate(-14deg)"></div>
  <div class="photo" role="img" aria-label="Photo of a man raising his fist on a rocky peak at golden sunrise" style="left:98px;top:1868px;width:469px;height:325px;background:linear-gradient(180deg,#f2c96e,#e3a859 55%,#8a7f62)"></div>
  <h2 class="heading" style="left:645px;top:1904px;width:460px">Get Weekly Reports on Your Progress and Goal Achievement</h2>
  <p class="copy" style="left:643px;top:2045px;width:440px">Celebrate your success each week as you review your progress on each life balance area.</p>
  <a class="btn" style="left:644px;top:2125px;width:139px">LEARN MORE</a>
</section>

<footer>
  <div class="abs brand" style="left:490px;top:2374px">
    <span class="brand-dot"></span><span class="brand-name">HARBOR GLOW LIVING</span>
  </div>
  <div class="footer-rule"></div>
  <p class="legal">COPYRIGHT © 2020 COMPANY ALL RIGHTS RESERVED.</p>
  <span class="social" style="left:981px;background:var(--blue)"></span>
  <span class="social" style="left:1015px;background:var(--pink)"></span>
  <span class="social" style="left:1049px;background:var(--blue)"></span>
  <span class="social" style="left:1083px;background:var(--sky)"></span>
</footer>
</body>
</html>
```